Präsentationsvorlagen / Powerpoint Master for my company
Zielgruppe
Offline hardware device to manage and save passwords safely.
Aufgabenstellung
DIN A4 quer

```html
<!DOCTYPE html>
<html lang="en">
<head>
<meta charset="utf-8">
<title>Lockwen – Presentation Master</title>
<link href="https://fonts.googleapis.com/css2?family=Montserrat:wght@300;400;500;700;800&display=swap" rel="stylesheet">
<style>
  :root {
    --green: #2f7a3b;
    --ink: #141414;
    --paper: #f1f1f2;
    --paper-shade: #e6e6e8;
    --body-text: #3a3a3a;
    --stage: #f3f3f3;
    --white: #ffffff;
  }
  * { box-sizing: border-box; margin: 0; padding: 0; }
  html, body {
    width: 909px; height: 1200px; overflow: hidden;
    background: var(--stage);
    font-family: "Montserrat", Arial, sans-serif;
  }
  h1, h2 { font-size: 1em; font-weight: inherit; }
  .canvas { position: relative; width: 909px; height: 1200px; }

  /* ---------- slide base (all sizes in em) ---------- */
  .slide {
    position: absolute;
    width: 40.4em; height: 28.6em;
    background: linear-gradient(100deg, var(--paper-shade) 0%, var(--paper) 25%, #f4f4f5 100%);
    overflow: hidden;
    box-shadow: 0 2px 10px rgba(0,0,0,.12);
  }
  .slide--thumb { font-size: 10px; }
  .slide--master { font-size: 18.3px; }

  .slide__header {
    position: absolute; left: 2.2em; top: 2.1em;
    font-size: 1.25em; font-weight: 700; color: var(--ink);
    white-space: nowrap;
  }
  .slide__header .accent { color: var(--green); }

  .brand {
    position: absolute; right: 2em; top: 1.7em;
    display: flex; align-items: center; gap: .35em;
    font-size: 1.7em; font-weight: 800; color: var(--ink);
    letter-spacing: -.01em; line-height: 1.2;
  }
  .brand__mark { width: .55em; height: .55em; background: var(--green); }
  .brand--light { color: var(--white); }

  .footer-band {
    position: absolute; left: 0; right: 0; bottom: 0; height: 1.5em;
    background: var(--ink);
    display: flex; align-items: center; padding-left: 2em;
  }
  .footer-band__title { font-size: .65em; font-weight: 700; color: var(--white); }
  .page-tab {
    position: absolute; right: 0; bottom: 0;
    width: 5.4em; height: 2em;
    background: var(--green);
    border-top-left-radius: 1em;
    display: flex; align-items: center; justify-content: center;
  }
  .page-tab__number { font-size: .95em; font-weight: 700; color: var(--white); }

  .photo { position: absolute; }
  .tri { position: absolute; background: var(--green); }
  .tri--down-left { clip-path: polygon(0 0, 100% 100%, 0 100%); }
  .tri--up-right  { clip-path: polygon(100% 0, 100% 100%, 0 100%); }
  .tri--top-left  { clip-path: polygon(0 0, 100% 0, 0 100%); }

  .kicker { position: absolute; line-height: 1.05; }
  .kicker__light { display: block; font-size: 1.6em; font-weight: 300; color: var(--ink); }
  .kicker__bold  { display: block; font-size: 1.6em; font-weight: 700; color: var(--green); }

  .copy {
    position: absolute;
    font-size: .5em; line-height: 1.55; color: var(--body-text);
  }

  .feature { position: absolute; width: 10em; }
  .feature__icon { width: 1.6em; height: 1.6em; margin-bottom: .4em; }
  .feature__title { font-size: .7em; font-weight: 700; color: var(--green); margin-bottom: .4em; }
  .feature__text { font-size: .5em; line-height: 1.55; color: var(--body-text); }

  /* ---------- cover ---------- */
  .slide--cover { background: #1b1b1c; }
  .cover__photo {
    position: absolute; inset: 0;
    background: linear-gradient(120deg, #1a1a1b 0%, #2b2b2c 45%, #3a3a3b 70%, #202021 100%);
  }
  .slide--cover .brand { left: 4.4em; right: auto; top: 4.4em; }
  .cover__title {
    position: absolute; left: 7.5em; top: 10.4em;
    color: var(--white); line-height: 1.1; white-space: nowrap;
  }
  .cover__title-light { display: block; font-size: 1.55em; font-weight: 400; }
  .cover__title-bold  { display: block; font-size: 1.55em; font-weight: 800; }
  .cover__copy {
    position: absolute; left: 15em; top: 31.2em; width: 42em;
    font-size: .5em; line-height: 1.6; color: #cfcfcf;
  }
  .slide--cover .page-tab { height: 1.7em; width: 6em; }
</style>
</head>
<body>
<main class="canvas">

  <!-- Cover slide -->
  <section class="slide slide--thumb slide--cover" style="left:40px; top:30px;">
    <div class="cover__photo" role="img" aria-label="Dark black and white photo of an office interior with large windows"></div>
    <div class="brand brand--light"><span class="brand__mark"></span>Lockwen</div>
    <h1 class="cover__title">
      <span class="cover__title-light">Your Presentation</span>
      <span class="cover__title-bold">Title Goes Here</span>
    </h1>
    <p class="cover__copy">A short overview of our offline device that keeps every password stored safely away from the network.</p>
    <div class="page-tab"></div>
  </section>

  <!-- Slide 02: text + photo -->
  <section class="slide slide--thumb" style="left:464px; top:30px;">
    <h2 class="slide__header"><span class="accent">Header</span> Goes Here</h2>
    <div class="brand"><span class="brand__mark"></span>Lockwen</div>
    <div class="kicker" style="left:3.2em; top:8.6em;">
      <span class="kicker__light">Lorem</span>
      <span class="kicker__bold">Ipsum Dolor</span>
    </div>
    <p class="copy" style="left:6.4em; top:26em; width:30em;">Our offline vault stores your passwords on the device itself, never in the cloud. Every entry stays encrypted and under your full control, wherever you carry it.</p>
    <div class="photo" role="img" aria-label="Photo of two colleagues talking in a bright workshop" style="left:21em; top:6.8em; width:16.6em; height:14.6em; background:linear-gradient(135deg,#c9ced6,#7f8a97 55%,#4b5461);"></div>
    <div class="tri tri--top-left" style="left:21em; top:6.8em; width:2.2em; height:2.2em;"></div>
    <div class="tri tri--up-right" style="left:35.4em; top:4.6em; width:2.2em; height:2.2em;"></div>
    <div class="footer-band"><span class="footer-band__title">Lockwen Presentation Title 2023</span></div>
    <div class="page-tab"><span class="page-tab__number">02</span></div>
  </section>

  <!-- Slide 03: photos + three features -->
  <section class="slide slide--thumb" style="left:40px; top:336px;">
    <h2 class="slide__header"><span class="accent">Header</span> Goes Here</h2>
    <div class="brand"><span class="brand__mark"></span>Lockwen</div>
    <div class="photo" role="img" aria-label="Photo of a presenter speaking in front of a screen" style="left:2.2em; top:7.6em; width:11em; height:7.8em; background:linear-gradient(135deg,#8a6a4c,#b08d68 50%,#556c86);"></div>
    <div class="photo" role="img" aria-label="Photo of a team listening in an open office with brick walls" style="left:13.6em; top:6em; width:24.6em; height:8em; background:linear-gradient(120deg,#a47c58,#c9a581 45%,#8a8d92 80%,#5f6268);"></div>
    <div class="tri tri--down-left" style="left:2.2em; top:13.2em; width:2.2em; height:2.2em;"></div>
    <div class="tri tri--up-right" style="left:36em; top:3.8em; width:2.2em; height:2.2em;"></div>

    <div class="feature" style="left:4.2em; top:16.4em;">
      <svg class="feature__icon" viewBox="0 0 24 24" fill="none" stroke="var(--green)" stroke-width="1.6"><circle cx="12" cy="12" r="9"/><path d="M7.5 12.5l3 3 6-6.5"/></svg>
      <div class="feature__title">Lorem ipsum</div>
      <p class="feature__text">Set up the device in minutes and move your saved logins over safely.</p>
    </div>
    <div class="feature" style="left:16em; top:15.2em;">
      <svg class="feature__icon" viewBox="0 0 24 24" fill="none" stroke="var(--green)" stroke-width="1.6"><path d="M12 3l7.5 3v5.5c0 4.6-3.2 8-7.5 9.5-4.3-1.5-7.5-4.9-7.5-9.5V6z"/></svg>
      <div class="feature__title">Lorem ipsum</div>
      <p class="feature__text">Encrypted storage keeps each password locked, even if the device is lost.</p>
    </div>
    <div class="feature" style="left:27.8em; top:15.2em;">
      <svg class="feature__icon" viewBox="0 0 24 24" fill="none" stroke="var(--green)" stroke-width="1.6"><path d="M3 21h18"/><rect x="5" y="13" width="3" height="8"/><rect x="10.5" y="9" width="3" height="12"/><rect x="16" y="5" width="3" height="16"/></svg>
      <div class="feature__title">Lorem ipsum</div>
      <p class="feature__text">Clear reports show how strong your passwords are and what to update.</p>
    </div>

    <div class="footer-band"><span class="footer-band__title">Lockwen Presentation Title 2023</span></div>
    <div class="page-tab"><span class="page-tab__number">03</span></div>
  </section>

  <!-- Slide 04: photo + text -->
  <section class="slide slide--thumb" style="left:464px; top:336px;">
    <h2 class="slide__header" style="top:4.6em;"><span class="accent">Header</span> Goes Here</h2>
    <div class="brand"><span class="brand__mark"></span>Lockwen</div>
    <div class="photo" role="img" aria-label="Photo of a hand holding an old telephone receiver" style="left:0; top:8.4em; width:17.6em; height:18.7em; background:linear-gradient(135deg,#d6d9dc,#8d9296 50%,#3d4044);"></div>
    <div class="tri tri--down-left" style="left:17.6em; top:15.8em; width:2.2em; height:2.2em;"></div>
    <div class="kicker" style="left:20.4em; top:7em;">
      <span class="kicker__light">Lorem</span>
      <span class="kicker__bold">Ipsum Dolor</span>
    </div>
    <p class="copy" style="left:40.8em; top:23.6em; width:31em;">No network, no sync, no remote access. The device works entirely offline, so your passwords can only be opened by the person holding it.</p>
    <div class="footer-band"><span class="footer-band__title">Lockwen Presentation Title 2023</span></div>
    <div class="page-tab"><span class="page-tab__number">04</span></div>
  </section>

  <!-- Master slide -->
  <section class="slide slide--master" style="left:84px; top:652px;">
    <h2 class="slide__header"><span class="accent">Header</span> Goes Here</h2>
    <div class="brand"><span class="brand__mark"></span>Lockwen</div>
    <div class="footer-band"><span class="footer-band__title">Lockwen Presentation Title 2023</span></div>
    <div class="page-tab"><span class="page-tab__number">03</span></div>
  </section>

</main>
</body>
</html>
```